Builders Worksite Corflute Outdoor Sign

We are a building company who are just branching out into new construction. How first new build is our own home which was designed by us and a local architect. We are proud and want to create more advertisement around our business.

We need a corflute sign that can staked outside the construction site and can be seen by people passing by.
Updates

Can we please make the company name and logo bigger (Tidewater Ridge Homes) This needs to be the focus. Can we please replace 'Manu' with 'Contact Us on 021-574-3619'

Target Market(s)

Home owners and people wishing to build on lifestyle blocks in New Zealand.

Font styles to use
Sans Serif

Requirements
Must have
• It needs to feature our:
Logo
Company name
Contact name and number - Manu - 0215743619
Landscape NOT portrait.

```html
<!DOCTYPE html>
<html lang="en">
<head>
<meta charset="utf-8">
<title>Tidewater Ridge Homes – Worksite Sign</title>
<link rel="stylesheet" href="https://fonts.googleapis.com/css2?family=Jost:wght@400;500&family=Poppins:wght@300;400;700&display=swap">
<style>
  :root {
    --navy: #151e2f;
    --gold: #f2bc1b;
    --gold-deep: #d99f24;
    --cream: #fcf4da;
    --white: #ffffff;
    --backdrop: #eceee9;
  }
  html, body {
    margin: 0;
    padding: 0;
    width: 1200px;
    height: 1200px;
    overflow: hidden;
    background: var(--backdrop);
  }
  .canvas {
    position: relative;
    width: 1200px;
    height: 1200px;
  }
  .sign {
    position: absolute;
    left: 30px;
    top: 220px;
    width: 1140px;
    height: 759px;
    box-shadow: 0 10px 30px rgba(0,0,0,0.12);
  }
  .sign svg { display: block; width: 100%; height: 100%; }
  .brand-name { font-family: "Jost", sans-serif; font-weight: 500; fill: var(--navy); }
  .contact-label { font-family: "Poppins", sans-serif; font-weight: 400; fill: var(--white); letter-spacing: 1px; }
  .contact-phone { font-family: "Poppins", sans-serif; font-weight: 700; fill: var(--white); }
  .web-address { font-family: "Poppins", sans-serif; font-weight: 300; fill: var(--white); }
  .web-address .web-bold { font-weight: 700; }
</style>
</head>
<body>
<main class="canvas">
  <section class="sign" aria-label="Tidewater Ridge Homes worksite sign">
    <svg viewBox="0 0 1142 760" xmlns="http://www.w3.org/2000/svg">
      <defs>
        <linearGradient id="gold-fill" x1="0" y1="0" x2="0" y2="1">
          <stop offset="0" stop-color="var(--gold)"/>
          <stop offset="1" stop-color="var(--gold-deep)"/>
        </linearGradient>
        <clipPath id="dome-clip">
          <path d="M135 590 C170 390 350 262 570 262 C790 262 970 390 1005 590 C990 660 940 720 880 760 L260 760 C200 720 150 660 135 590 Z"/>
        </clipPath>
      </defs>

      <!-- sign board -->
      <rect class="board" x="0" y="0" width="1142" height="760" fill="url(#gold-fill)"/>

      <!-- top corner panels -->
      <polygon class="corner-left" points="0,0 214,0 38,218 0,218" fill="var(--navy)"/>
      <polygon class="corner-right" points="928,0 1142,0 1142,228 1106,228" fill="var(--navy)"/>

      <!-- house silhouette -->
      <polygon class="house-roof" points="236,0 908,0 1086,218 1000,218 1000,234 145,234 145,218 58,218" fill="var(--white)"/>
      <path class="house-walls" d="M90 230 L1052 230 L1052 380 C1052 520 1010 650 880 760 L260 760 C130 650 90 520 90 380 Z" fill="var(--white)"/>
      <polygon class="house-glow" points="572,40 1052,420 1052,640 90,640 90,420" fill="var(--cream)"/>

      <!-- contact dome -->
      <path class="dome-ring" d="M116 600 C150 370 340 242 570 242 C800 242 990 370 1024 600 L1010 640 L130 640 Z" fill="var(--white)"/>
      <path class="dome" d="M135 590 C170 390 350 262 570 262 C790 262 970 390 1005 590 C990 660 940 720 880 760 L260 760 C200 720 150 660 135 590 Z" fill="url(#gold-fill)"/>
      <rect class="web-band" x="0" y="648" width="1142" height="112" fill="var(--navy)" clip-path="url(#dome-clip)"/>

      <!-- emblem spot -->
      <circle class="emblem-dot" cx="569" cy="300" r="58" fill="var(--navy)"/>

      <!-- company name -->
      <text class="brand-name" x="571" y="96" font-size="58" text-anchor="middle" letter-spacing="1">TIDEWATER RIDGE</text>
      <text class="brand-name" x="571" y="164" font-size="40" text-anchor="middle" letter-spacing="14">HOMES</text>

      <!-- contact -->
      <line class="rule" x1="245" y1="465" x2="395" y2="465" stroke="var(--white)" stroke-width="3"/>
      <line class="rule" x1="750" y1="465" x2="900" y2="465" stroke="var(--white)" stroke-width="3"/>
      <text class="contact-label" x="572" y="478" font-size="40" text-anchor="middle">CONTACT MANU</text>
      <text class="contact-phone" x="572" y="585" font-size="88" text-anchor="middle">021-574-3619</text>

      <!-- website -->
      <text class="web-address" x="571" y="718" font-size="32" text-anchor="middle">WWW.<tspan class="web-bold">TIDEWATERRIDGEHOMES</tspan>.COM</text>
    </svg>
  </section>
</main>
</body>
</html>
```